Redesign of LumaWireHub.com website

Revised description:
We would like to redesign our 8 year old website (in Pagecraft) to something fresh and current. Although I've attached our log, we are open to a new logo if you have a cool idea but it should have lumawirehub.com somewhere in the logo.  We are going to eventually put 5 rotating images on the homepage but for the interest of this design contest, I would like you to use  just one image (#23), only on the small laptop screen in the image, I would like to see the lumawirehub homepage inserted (that you've designed) giving the illusion that whoever was using that laptop was looking at the lumawirehub website. The tagline "your high-end equipment deserves high-end cables." should be somewhere on the image as well.
This is an open slate, we are open to new colors, designs, etc. We really want something simple, not crowded with images, etc.
I have included a bunch of pictures to use or you can use your own. You can use the same product categories that we currently have on the website. There should also be a place on the homepage to insert our Vidstream video.
We sell to businesses and get a lot of orders from the government and military so the site should be catered towards this market. We sell very little to consumers. Our biggest competitor is q7v.com but we don't really want something that looks like their site. Something closer to a tobe.com or kp.com is more what we're looking for. Please keep in mind that we also want people to know its a retail site, where they can purchase cables. The winner of this will likely have additional $$ work as we will be making a lot of product changes in the near future.

Target Market(s)
We sell fiber optic and copper cables to Government agencies, military, colleges/universities, small & large businesses. Mostly male. 25-50.
Industry/Entity Type
Government
Requirements
Must have
- We are different from our competition in the following ways:
1. FREE ground shipping on ALL orders
2. We build custom cables in the USA
3. We have a lifetime warranty on ALL of our cables so we use the highest quality components
4. We are on the west coast so we have up to 3 extra hours to ship our product for same day shipping
5. We stock over 100,000 different cables
6. Our prices are competitive
You can watch our Vidstream video to get an idea : )
Nice to have
- I've included a lot of images below for inspiration or to use on the site when appropriate.
Here is a site that I really like. You need to cut and paste it.
http://layoutbazaar.example/item/velora-site-theme-a-shop-theme/full_screen_preview/774310
Should not have
- Anything "cartoony" or whimsical.

```html
<!DOCTYPE html>
<html lang="en">
<head>
<meta charset="utf-8">
<title>LumaWireHub.com — High-End Cables</title>
<link href="https://fonts.googleapis.com/css2?family=Arimo:ital,wght@0,400;0,700;1,400&family=Source+Sans+3:wght@400;600&display=swap" rel="stylesheet">
<style>
:root{
  --red:#d7141c;
  --blue:#0a8fdc;
  --blue-dark:#0570b8;
  --ink:#333;
  --muted:#6b6b6b;
  --grey-head:#7c8385;
  --panel:#e6e6e6;
  --footer:#b3b3b3;
  --white:#fff;
}
*{box-sizing:border-box;margin:0;padding:0}
html,body{width:737px;height:1200px;overflow:hidden;background:var(--white)}
body{position:relative;font-family:"Arimo",Arial,sans-serif;color:var(--ink)}
.abs{position:absolute}

/* header */
.top-rule{left:0;top:0;width:737px;height:3px;background:#e4636a}
.header{left:0;top:3px;width:737px;height:91px;background:linear-gradient(#fff 55%,#ececec)}
.brand{left:60px;top:28px;display:flex;align-items:center;gap:7px}
.brand-dot{width:14px;height:14px;border-radius:50%;background:var(--blue)}
.brand-name{font-family:"Source Sans 3",sans-serif;font-weight:600;font-size:24px;color:var(--red);letter-spacing:-.3px}
.cart{left:516px;top:6px;width:159px;height:27px;background:#e3e3e3;border-radius:0 0 3px 3px;font-size:7.5px;display:flex;align-items:center;padding-left:22px;gap:6px}
.util{right:65px;top:58px;font-size:7.5px;color:#444;white-space:nowrap}
.util a{color:#444;text-decoration:none}
.util .hl{color:var(--blue)}
.nav{left:0;top:97px;width:737px;height:33px;background:#fff;border-bottom:4px solid #e5e5e5}
.nav-home{left:64px;top:6px;width:57px;height:19px;background:var(--blue);color:#fff;font-size:9px;display:flex;align-items:center;justify-content:center}
.nav-item{top:10px;font-size:9px;color:#222}
.nav-sep{top:5px;width:0;height:21px;border-left:1px dotted #bbb}
.search{left:528px;top:7px;width:146px;height:19px;border:1px solid #ccc;border-radius:10px;background:linear-gradient(#f3f3f3,#fff);font-size:6.5px;color:#888;padding:6px 0 0 7px}

/* hero */
.hero{left:0;top:134px;width:737px;height:306px;background:linear-gradient(#fff 45%,#e9e9e9);border-bottom:1px solid #ddd}
.hero-media{left:62px;top:44px;width:254px;height:167px;background:linear-gradient(125deg,#2a2a33 0%,#6d6d76 30%,#d9c94a 50%,#6bb36d 62%,#c86fb4 72%,#eaeaea 100%);border-radius:4px 40px 60px 8px;opacity:.9}
.hero-arrow{top:140px;width:18px;height:27px;background:#1b1b1b}
.hero-title{left:332px;top:91px;font-family:"Source Sans 3",sans-serif;font-weight:400;font-size:19px;color:var(--red);line-height:1}
.hero-title-2{left:336px;top:114px;font-family:"Source Sans 3",sans-serif;font-weight:400;font-size:23px;color:var(--red);line-height:1}
.hero-copy{left:337px;top:144px;width:290px;font-size:7.4px;line-height:12px;color:#444}
.btn-more{left:334px;top:194px;width:104px;height:28px;border-radius:9px;background:linear-gradient(#3fb0f0,var(--blue-dark));color:#fff;font-family:"Source Sans 3",sans-serif;font-size:12px;display:flex;align-items:center;justify-content:center;gap:9px;box-shadow:0 4px 4px -2px #8aa}

/* products */
.section-title{left:0;width:737px;text-align:center;top:475px;font-family:"Source Sans 3",sans-serif;font-weight:600;font-size:16px;color:var(--grey-head)}
.round-arrow{top:590px;width:14px;height:14px;border-radius:50%;background:#8d8d8d}
.thumb{border:2px solid #ddd;background:#fff;padding:1px}
.thumb span{display:block;width:100%;height:100%}
.prod-name{font-size:8px;font-weight:700;color:#333;text-align:center}
.prod-sub{font-size:7px;color:#666;text-align:center}
.prod-price{font-size:7.5px;color:var(--red);text-align:center}
.feature-card{left:190px;top:541px;width:123px;height:139px;background:#fff;border:1px solid #e2e2e2;border-radius:6px;box-shadow:0 0 4px #ddd;overflow:hidden}
.feature-cap{position:absolute;left:1px;bottom:1px;width:120px;height:32px;background:var(--blue);color:#fff;font-size:6.2px;line-height:10px;padding:6px 8px;border-radius:0 0 5px 5px}

/* info panel */
.panel{left:0;top:738px;width:737px;height:254px;background:var(--panel);border-top:1px dotted #bbb}
.panel-head{top:758px;font-family:"Source Sans 3",sans-serif;font-weight:600;font-size:15.5px}
.video{left:62px;top:793px;width:176px;height:87px;background:#fff;border:1px solid #ccc;padding:6px}
.video-screen{width:100%;height:100%;background:radial-gradient(circle at 50% 55%,#8a5a24,#2b1b10 55%,#0d0d0d)}
.video-intro{left:61px;top:891px;width:180px;font-size:7px;line-height:11px;color:#333}
.btn-read{left:65px;top:934px;width:59px;height:17px;border-radius:2px;background:linear-gradient(#1fa2ef,#0562b0);color:#fff;font-family:"Source Sans 3",sans-serif;font-weight:600;font-size:10px;display:flex;align-items:center;justify-content:center}
.perk{left:313px;height:24px;background:#f4f4f4;font-family:"Source Sans 3",sans-serif;font-size:12px;color:#555;padding:4px 8px;white-space:nowrap}
.perk.active{background:var(--blue);color:#fff;height:34px;line-height:15px;padding:2px 8px;white-space:normal}

/* testimonial */
.testimonial{left:0;top:993px;width:737px;height:128px;background:var(--blue)}
.avatar{left:62px;top:27px;width:80px;height:80px;border-radius:50%;border:3px solid #fff;background:linear-gradient(#cfd6dc,#8a969e)}
.quote{left:153px;top:48px;width:525px;font-style:italic;font-size:8.2px;line-height:14.5px;color:#e8f4fd}
.quote-by{left:153px;top:96px;font-size:7.5px;font-weight:700;color:#fff}

/* footer */
.footer{left:0;top:1121px;width:737px;height:79px;background:var(--footer)}
.foot-links{left:0;width:737px;top:14px;text-align:center;font-family:"Source Sans 3",sans-serif;font-size:8px;color:#fff}
.foot-copy{left:0;width:737px;top:26px;text-align:center;font-family:"Source Sans 3",sans-serif;font-size:8px;color:#fff}
.social{top:45px;width:19px;height:19px;border-radius:50%}
</style>
</head>
<body>

<div class="abs top-rule"></div>
<header class="abs header">
  <div class="abs brand"><span class="brand-dot"></span><span class="brand-name">lumawirehub.com</span></div>
  <div class="abs cart">
    <svg width="16" height="13" viewBox="0 0 16 13"><path d="M1 1h3l2 7h7l2-5H5" fill="none" stroke="#e08a18" stroke-width="1.6"/><circle cx="7" cy="11" r="1.3" fill="#555"/><circle cx="12" cy="11" r="1.3" fill="#555"/></svg>
    <span>My cart: &nbsp;&nbsp;1 item(s) &nbsp;| &nbsp;$ 270</span>
  </div>
  <div class="abs util"><a href="#">My Account</a> &nbsp;| &nbsp;<a href="#">View Shopping Bag</a> &nbsp;(0 items ) | <a class="hl" href="#">Go to Checkout</a> &nbsp;&nbsp;&nbsp;<a href="#">Login</a> &nbsp;| &nbsp;&nbsp;<a href="#">Register</a></div>
</header>

<nav class="abs nav">
  <div class="abs nav-home">HOME</div>
  <span class="abs nav-sep" style="left:127px"></span>
  <span class="abs nav-item" style="left:148px">SECURITY</span>
  <span class="abs nav-sep" style="left:215px"></span>
  <span class="abs nav-item" style="left:226px">HOW IT WORK</span>
  <span class="abs nav-sep" style="left:310px"></span>
  <span class="abs nav-item" style="left:320px">FEATURES</span>
  <span class="abs nav-sep" style="left:389px"></span>
  <span class="abs nav-item" style="left:406px">SUPPORT</span>
  <div class="abs search">Search Products
    <svg class="abs" style="left:127px;top:3px" width="11" height="11" viewBox="0 0 11 11"><circle cx="4.5" cy="4.5" r="3.3" fill="none" stroke="#333" stroke-width="1.2"/><path d="M7 7l3 3" stroke="#333" stroke-width="1.6"/></svg>
  </div>
</nav>

<section class="abs hero">
  <div class="abs hero-media" role="img" aria-label="Cut-away fibre optic cable showing coloured inner strands"></div>
  <div class="abs hero-arrow" style="left:63px"><svg width="18" height="27" viewBox="0 0 18 27"><path d="M12 6l-6 7.5 6 7.5" fill="none" stroke="#fff" stroke-width="2.2"/></svg></div>
  <div class="abs hero-arrow" style="left:655px"><svg width="18" height="27" viewBox="0 0 18 27"><path d="M6 6l6 7.5-6 7.5" fill="none" stroke="#fff" stroke-width="2.2"/></svg></div>
  <h1 class="abs hero-title">YOUR HIGH-END EQUIPMENT DESERVES</h1>
  <h2 class="abs hero-title-2">HIGH-END CABLES</h2>
  <p class="abs hero-copy">Lorem ipsum dolor sit amet, consectetur adipiscing elit. Quisque dapibus accumsan orci, pretium eleifend arcu adipiscing eget. Fusce accumsan facilisis tincidunt. Pha-sellus tempor enim purus, vitae venenatis est. Ut imperdiet hendrerit pulvinar. Cras at</p>
  <div class="abs btn-more">Read More <svg width="7" height="10" viewBox="0 0 7 10"><path d="M1 1l4 4-4 4" fill="none" stroke="#fff" stroke-width="1.4"/></svg></div>
</section>

<h2 class="abs section-title">New Products On Fibre Cables</h2>
<div class="abs round-arrow" style="left:62px"><svg width="14" height="14" viewBox="0 0 14 14"><path d="M8 4l-3 3 3 3" fill="none" stroke="#fff" stroke-width="1.6"/></svg></div>
<div class="abs round-arrow" style="left:645px"><svg width="14" height="14" viewBox="0 0 14 14"><path d="M6 4l3 3-3 3" fill="none" stroke="#fff" stroke-width="1.6"/></svg></div>

<div class="abs thumb" style="left:93px;top:565px;width:98px;height:65px"><span role="img" aria-label="Blue patch cables with connectors" style="background:linear-gradient(#eef3f8,#8fb0d2)"></span></div>
<div class="abs prod-name" style="left:93px;top:640px;width:98px">High End Cables</div>
<div class="abs prod-sub" style="left:93px;top:651px;width:98px">Lorem Ipsum</div>
<div class="abs prod-price" style="left:93px;top:661px;width:98px">$ 125.000</div>

<div class="abs feature-card">
  <span class="abs" role="img" aria-label="Green fibre connectors with yellow leads" style="left:8px;top:13px;width:107px;height:62px;background:linear-gradient(#f6f4d4,#8fcf72 70%,#2e9a3e)"></span>
  <div class="abs prod-sub" style="left:0;top:82px;width:123px;font-size:7.2px">Promotional Picnic Sets</div>
  <div class="abs prod-price" style="left:0;top:92px;width:123px;color:var(--blue)">$ 125.000</div>
  <div class="feature-cap">Valuable branded picnic sets draw attention with a custom...</div>
</div>

<div class="abs thumb" style="left:311px;top:567px;width:103px;height:65px"><span role="img" aria-label="Patch panel with green fibre connectors" style="background:linear-gradient(#2f3a2e,#4e9a45 60%,#2a2f2a)"></span></div>
<div class="abs prod-name" style="left:306px;top:641px;width:100px">High End Cables</div>
<div class="abs prod-sub" style="left:306px;top:652px;width:100px">Lorem Ipsum</div>
<div class="abs prod-price" style="left:306px;top:662px;width:100px">$ 125.000</div>

<div class="abs thumb" style="left:420px;top:567px;width:105px;height:65px"><span role="img" aria-label="Blue fibre connectors with yellow leads" style="background:linear-gradient(#1e4fa8,#3b8ee0 55%,#cfd8c9)"></span></div>
<div class="abs prod-name" style="left:420px;top:641px;width:100px">High End Cables</div>
<div class="abs prod-sub" style="left:420px;top:652px;width:100px">Lorem Ipsum</div>
<div class="abs prod-price" style="left:420px;top:662px;width:100px">$ 125.000</div>

<div class="abs thumb" style="left:532px;top:566px;width:104px;height:66px"><span role="img" aria-label="Green fibre connectors with yellow leads" style="background:linear-gradient(#f6f4d4,#8fcf72 70%,#2e9a3e)"></span></div>
<div class="abs prod-name" style="left:530px;top:642px;width:100px">High End Cables</div>
<div class="abs prod-sub" style="left:530px;top:653px;width:100px">Lorem Ipsum</div>
<div class="abs prod-price" style="left:530px;top:663px;width:100px">$ 125.000</div>

<section class="abs panel"></section>
<h2 class="abs panel-head" style="left:61px;color:var(--blue)">Watch Our <span style="color:var(--red)">Latest Vedio</span></h2>
<div class="abs video">
  <div class="video-screen" role="img" aria-label="Video still of two fibre connectors on a dark background"></div>
  <svg class="abs" style="left:78px;top:33px" width="20" height="20" viewBox="0 0 20 20"><circle cx="10" cy="10" r="9" fill="none" stroke="#fff" stroke-width="1.5"/><path d="M8 6l6 4-6 4z" fill="#fff"/></svg>
</div>
<p class="abs video-intro">We are a new company that showcases beautiful products available from neighborhood merchants. Our front page allowsy.</p>
<div class="abs btn-read">Read</div>

<h2 class="abs panel-head" style="left:314px;color:#666">What Makes Us Different From Others</h2>
<div class="abs perk" style="top:789px;width:221px">"FREE ground shipping on ALL orders"</div>
<div class="abs perk" style="top:821px;width:231px">"We build custom cables in the USA"</div>
<div class="abs perk" style="top:853px;width:298px">"We have a lifetime warranty on ALL of our cables</div>
<div class="abs perk active" style="top:885px;width:362px">"We are on the west coast so we have up to 3 extra hours to ship our product for same day shipping"</div>
<div class="abs perk" style="top:925px;width:297px">"We stock over 100,000 different cables</div>

<section class="abs testimonial">
  <div class="abs avatar" role="img" aria-label="Customer portrait"></div>
  <p class="abs quote">"Itaque earum rerum hic tenetur a sapiente delectus, ut aut reiciendis voluptatibus maiores alias consequatur aut perferendis doloribus asperiores repellat.Sed ut perspicis unde omnis iste natus error siuptatem accusantium doloremque laudantium, totam rem aperiam, eaque ipsab illo inventore."</p>
  <div class="abs quote-by">- DALE RENNER</div>
  <svg class="abs" style="left:644px;top:102px" width="30" height="16" viewBox="0 0 30 16"><path d="M10 2L4 8l6 6M20 2l6 6-6 6" fill="none" stroke="#3a3a3a" stroke-width="2.6"/></svg>
</section>

<footer class="abs footer">
  <div class="abs foot-links">Terms &amp; Conditions &nbsp;&nbsp;| &nbsp;&nbsp;Privacy &amp; Security &nbsp;&nbsp;| &nbsp;&nbsp;About Us &nbsp;&nbsp;| Contact Us</div>
  <div class="abs foot-copy">© 2012 Copyright &nbsp;LumaWire Hub</div>
  <span class="abs social" style="left:312px;background:#1e2a44"></span>
  <span class="abs social" style="left:335px;background:#1d8fe0"></span>
  <span class="abs social" style="left:359px;background:#f07a1a"></span>
  <span class="abs social" style="left:382px;background:#8c8c8c"></span>
</footer>

</body>
</html>
```